wedding photography website for top wedding photographer

I have a website right now that is barely working. I want the photos to maybe all the photos lined up horizontally and you scroll to see the images. I have an orange logo and want it to be dark grey. I also need a page for publications (I have those as scans) and a link to an About page.

Target Market(s)

wedding planners and bride

Industry/Entity Type

Wedding Photography

Coding

Coded - Design and coding required

Number of Pages Required

5+ page

Font styles to use
Serif
Sans Serif

Colors
ffffff
474747

Requirements
Must have
• easy to navigate, always want the instagram and contact info readily available, should be clean and modern and let the photos stand out. it's wedding photos but i don't want it to feel girly or prissy.
Nice to have
• possibly could be one big photo on the home page, then click it to go into all the other photos. want page options on the home page and every page
Should not have
• nothing fussy or quaint, want this to be the "Copper Ladle" restaurant of wedding photography

```html
<!DOCTYPE html>
<html lang="en">
<head>
<meta charset="utf-8">
<title>Ava Lorne Photography — Menu</title>
<link rel="stylesheet" href="https://fonts.googleapis.com/css2?family=Frank+Ruhl+Libre:wght@400;500&display=swap">
<style>
  :root {
    --ink: #474747;
    --paper: #ffffff;
    --rule: #5a5a5a;
    --faint: #d4d4d4;
    --icon: #8f8f8f;
    --leaf-light: #e7ece0;
    --leaf-mid: #c9d3bd;
    --leaf-deep: #aebb9f;
    --lawn: #c3ccb4;
    --sky: #f3f4ef;
    --veil: #fbfbfa;
  }
  * { margin: 0; padding: 0; box-sizing: border-box; }
  html, body {
    width: 1200px; height: 601px; overflow: hidden;
    background: var(--paper);
    font-family: "Frank Ruhl Libre", Georgia, serif;
    color: var(--ink);
  }
  .site { position: relative; width: 1200px; height: 601px; }

  .brand {
    position: absolute; left: 50px; top: 22px;
    font-size: 30px; font-weight: 400; letter-spacing: 0.2px;
    color: var(--ink); text-decoration: none;
  }

  .menu-close { position: absolute; left: 1128px; top: 36px; width: 22px; height: 22px; }

  .hero {
    position: absolute; left: 47px; top: 87px; width: 1105px; height: 450px;
    overflow: hidden;
    background:
      radial-gradient(ellipse 14% 55% at 47% 70%, var(--veil) 0%, rgba(251,251,250,0.7) 45%, transparent 100%),
      radial-gradient(ellipse 10% 40% at 55% 55%, rgba(120,120,125,0.35) 0%, transparent 100%),
      radial-gradient(ellipse 30% 35% at 15% 40%, var(--leaf-deep) 0%, transparent 100%),
      radial-gradient(ellipse 30% 35% at 85% 38%, var(--leaf-deep) 0%, transparent 100%),
      radial-gradient(ellipse 25% 20% at 35% 20%, var(--leaf-light) 0%, transparent 100%),
      linear-gradient(180deg, var(--sky) 0%, var(--leaf-mid) 22%, var(--leaf-deep) 55%, var(--lawn) 72%, var(--leaf-mid) 100%);
  }
  .hero-veil { position: absolute; inset: 0; background: rgba(255,255,255,0.6); }

  .hero-arrow {
    position: absolute; top: 202px; width: 36px; height: 46px;
    background: rgba(255,255,255,0.55);
    display: flex; align-items: center; justify-content: center;
  }
  .hero-arrow.prev { left: 0; }
  .hero-arrow.next { right: 0; }

  .main-nav { position: absolute; left: 0; top: 0; width: 1200px; height: 601px; }
  .main-nav a {
    position: absolute; left: 0; width: 1200px; text-align: center;
    font-size: 24px; font-weight: 500; letter-spacing: 0.8px;
    color: #2f2f2f; text-decoration: none; line-height: 1;
  }
  .nav-rule { position: absolute; left: 600px; width: 1px; background: var(--rule); }

  .site-footer { position: absolute; left: 0; top: 560px; width: 1200px; height: 24px; }
  .social-link {
    position: absolute; top: 6px; width: 12px; height: 12px;
    border-radius: 50%; background: var(--icon);
  }
  .footer-rule { position: absolute; left: 555px; top: 11px; width: 62px; height: 1px; background: #e4e4e4; }
  .copyright {
    position: absolute; left: 631px; top: 4px;
    font-size: 12px; color: var(--faint); letter-spacing: 0.2px;
  }
</style>
</head>
<body>
<div class="site">
  <a class="brand" href="#">Ava Lorne Photography</a>

  <svg class="menu-close" viewBox="0 0 22 22" aria-label="Close menu">
    <line x1="1" y1="1" x2="21" y2="21" stroke="#474747" stroke-width="1.6"/>
    <line x1="21" y1="1" x2="1" y2="21" stroke="#474747" stroke-width="1.6"/>
  </svg>

  <div class="hero" role="img" aria-label="Wedding photograph of a bride with a long veil embracing the groom on a garden lawn">
    <div class="hero-veil"></div>
    <div class="hero-arrow prev">
      <svg width="8" height="12" viewBox="0 0 8 12"><polyline points="6,1 1,6 6,11" fill="none" stroke="#b4b4b4" stroke-width="1.5"/></svg>
    </div>
    <div class="hero-arrow next">
      <svg width="8" height="12" viewBox="0 0 8 12"><polyline points="2,1 7,6 2,11" fill="none" stroke="#b4b4b4" stroke-width="1.5"/></svg>
    </div>
  </div>

  <nav class="main-nav">
    <a href="#" style="top:175px; left:4px;">About</a>
    <span class="nav-rule" style="top:209px; height:40px;"></span>
    <a href="#" style="top:254px;">Contact</a>
    <span class="nav-rule" style="top:285px; height:40px;"></span>
    <a href="#" style="top:333px;">Links</a>
    <span class="nav-rule" style="top:369px; height:39px;"></span>
    <a href="#" style="top:412px; left:-2px;">Publications</a>
  </nav>

  <footer class="site-footer">
    <a class="social-link" href="#" aria-label="Social profile one" style="left:473px;"></a>
    <a class="social-link" href="#" aria-label="Social profile two" style="left:503px;"></a>
    <a class="social-link" href="#" aria-label="Social profile three" style="left:532px;"></a>
    <span class="footer-rule"></span>
    <span class="copyright">Copyright © 2018</span>
  </footer>
</div>
</body>
</html>
```